Business Card Design

We need two business cards - same design but with two different people's details.

We are a new start-up online cleaning business that allows people to book and pay for a quality home cleaner online.

We would like a professional yet overly formal style of business card.

Target Market(s)

18 - 65+ professionals

Industry/Entity Type

Business

Contact Information for Business Card

We would like two business cards but with the same design, the details are below:

Mark Pelletta
Director and Co-Founder
ph: 0491 352 807
Suite 4C, Level 3
517 Larkfield Road
Brindale NSW 2093
mark@tidvane.com.au

_______________________________________________________

Evadne Pelletta
Director and Co-Founder
ph: 0427 915364
Suite 4C, Level 3
517 Larkfield Road
Brindale NSW 2093
evadne@tidvane.com.au

Requirements
Must have
• although our style guide refers to orange and red, please stick to the blue/black/grey that is in the style guide.

also on the back of the card we would like the logo with our tag line which is on page 12 of the style guide.
Should not have
• no pictures of mops, cleaners etc

```html
<!DOCTYPE html>
<html lang="en">
<head>
<meta charset="utf-8">
<title>Tidvane Business Card</title>
<link rel="stylesheet" href="https://fonts.googleapis.com/css2?family=Lato:wght@400;700;900&family=Quicksand:wght@400;500&display=swap">
<style>
  :root {
    --backdrop: #2b2b2d;
    --brand-blue: #04a6df;
    --brand-blue-deep: #0f86bf;
    --ink: #0d0d0d;
    --charcoal: #2f3031;
    --grey-text: #5e6264;
    --card-white: #f3f4f4;
  }
  * { box-sizing: border-box; margin: 0; padding: 0; }
  html, body {
    width: 1200px;
    height: 900px;
    overflow: hidden;
    background: var(--backdrop);
  }
  .stage { position: relative; width: 1200px; height: 900px; }

  .card {
    position: absolute;
    width: 560px;
    height: 340px;
    box-shadow: 0 12px 30px rgba(0,0,0,0.55);
  }

  /* Back of card */
  .card-back {
    left: 70px;
    top: 100px;
    background: var(--brand-blue);
    display: flex;
    align-items: center;
    padding-left: 70px;
    gap: 22px;
  }
  .card-back .brand-dot {
    width: 96px; height: 96px;
    border-radius: 50%;
    background: var(--ink);
    flex: none;
  }
  .card-back .brand-name {
    font-family: "Lato", sans-serif;
    font-weight: 900;
    font-size: 64px;
    line-height: 1;
    color: var(--ink);
    letter-spacing: -1px;
  }
  .card-back .tagline {
    font-family: "Quicksand", sans-serif;
    font-weight: 400;
    font-size: 19px;
    color: var(--ink);
    margin-top: 8px;
  }

  /* Front of card */
  .card-front {
    left: 570px;
    top: 470px;
    background: var(--card-white);
    display: flex;
  }
  .brand-block {
    width: 290px;
    display: flex;
    flex-direction: column;
    align-items: center;
    justify-content: center;
    gap: 18px;
  }
  .brand-block .brand-dot {
    width: 110px; height: 110px;
    border-radius: 50%;
    background: var(--brand-blue);
  }
  .brand-block .brand-name {
    font-family: "Lato", sans-serif;
    font-weight: 900;
    font-size: 62px;
    line-height: 1;
    color: var(--charcoal);
    letter-spacing: -1px;
  }
  .divider {
    width: 2px;
    margin: 70px 0 40px;
    background: linear-gradient(to bottom, rgba(90,90,90,0.1), #5a5a5a);
  }
  .details {
    padding: 36px 0 0 22px;
    font-family: "Lato", sans-serif;
  }
  .person-name {
    font-weight: 900;
    font-size: 15px;
    color: var(--brand-blue-deep);
    text-transform: uppercase;
    letter-spacing: 0.3px;
  }
  .person-role {
    font-weight: 700;
    font-size: 10.5px;
    color: var(--grey-text);
    margin-top: 2px;
  }
  .address {
    font-style: normal;
    font-weight: 900;
    font-size: 13px;
    line-height: 1.3;
    color: var(--brand-blue-deep);
    margin-top: 52px;
  }
  .contact-list { list-style: none; margin-top: 12px; }
  .contact-list li {
    display: flex;
    align-items: center;
    gap: 10px;
    font-size: 14px;
    color: var(--grey-text);
    margin-bottom: 9px;
    padding-left: 20px;
  }
  .contact-list svg { width: 14px; height: 12px; fill: var(--grey-text); flex: none; }
  .website {
    font-weight: 900;
    font-size: 15px;
    color: var(--brand-blue-deep);
    padding-left: 20px;
    margin-top: 4px;
  }
</style>
</head>
<body>
<main class="stage">

  <section class="card card-back" aria-label="Back of business card">
    <span class="brand-dot"></span>
    <div>
      <p class="brand-name">Tidvane</p>
      <p class="tagline">Save time. Book a quality cleaner online.</p>
    </div>
  </section>

  <section class="card card-front" aria-label="Front of business card">
    <div class="brand-block">
      <span class="brand-dot"></span>
      <p class="brand-name">Tidvane</p>
    </div>
    <div class="divider"></div>
    <div class="details">
      <p class="person-name">Mark Pelletta</p>
      <p class="person-role">Director &amp; Co-Founder</p>
      <address class="address">Suite 4C, Level 3 517 Larkfield<br>Road Brindale NSW 2093</address>
      <ul class="contact-list">
        <li>
          <svg viewBox="0 0 14 12" aria-hidden="true"><path d="M1 3 Q7 -1 13 3 L11 5 L9 3.5 L5 3.5 L3 5 Z M3 6 H11 L12.5 11 H1.5 Z"/></svg>
          0491 352 807
        </li>
        <li>
          <svg viewBox="0 0 14 12" aria-hidden="true"><path d="M0 1 H14 V11 H0 Z M1 2 L7 7 L13 2 Z" fill-rule="evenodd"/></svg>
          mark@tidvane.com.au
        </li>
      </ul>
      <p class="website">www.tidvane.com.au</p>
    </div>
  </section>

</main>
</body>
</html>
```